Business Cards for Law Office of Denise R. Harlow

I need a business card for my new estate planning law firm. I have attached my logo. I would like a design that is professional but not too formal or stuffy.

Target Market(s)

Professionals (lawyers, doctors, businesswomen) between the age of 30 and 50 who are tech-savvy and educated.

Industry/Entity Type

Lawyer

Contact Information for Business Card

Denise R. Harlow

528 E. 19th Street
7th Floor
New York, NY 10583

Phone: (855) 602-7318
Direct: (917) 463-5071
Email: Denise@DeniseRHarlowLegal.test
www.DeniseRHarlowLegal.test

Font styles to use
Other font styles liked:
• Corbel

Requirements
Must have
• On the front:
• Denise R. Harlow, Esq.
• Owner & Founder
• 528 E. 19th Street
• 7th Floor
• New York, NY 10583
• Phone: (855) 602-7318
• Direct: (917) 463-5071
• Email: denise@deniserharlowlegal.test
• www.deniserharlowlegal.test
• On the back:
• LOGO
Nice to have
• I want it to be professional but not too formal or stuffy. Please choose colors that go with my logo.
Should not have
• I don't want TOO MUCH color. Some color is good, but not too much.

```html
<!DOCTYPE html>
<html lang="en">
<head>
<meta charset="utf-8">
<title>Business Cards – Law Office of Denise R. Harlow</title>
<link rel="stylesheet" href="https://fonts.googleapis.com/css2?family=Cinzel:wght@400;500&family=Roboto:wght@400&display=swap">
<style>
  :root {
    --backdrop: #dcdcdc;
    --card: #ffffff;
    --plum: #6a1b6e;
    --accent: #e08a2c;
    --ink: #3a3a3a;
  }
  * { margin: 0; padding: 0; box-sizing: border-box; }
  html, body { width: 1200px; height: 576px; overflow: hidden; }
  body { background: var(--backdrop); position: relative; font-family: "Roboto", Arial, sans-serif; }

  .card {
    position: absolute;
    background: var(--card);
    border: 1px solid #cfcfcf;
  }
  .card--front { left: 94px; top: 139px; width: 484px; height: 293px; }
  .card--back  { left: 614px; top: 138px; width: 482px; height: 291px; }

  .firm-name {
    font-family: "Cinzel", "Times New Roman", serif;
    font-weight: 500;
    color: var(--plum);
    text-transform: uppercase;
    line-height: 1.2;
    position: absolute;
  }
  .card--front .firm-name {
    left: 0; right: 0; top: 112px;
    text-align: center;
    font-size: 26px;
    letter-spacing: 0.5px;
  }
  .card--back .firm-name {
    left: 30px; top: 108px; width: 210px;
    text-align: center;
    font-size: 17px;
  }

  .attorney-name {
    position: absolute;
    left: 264px; top: 86px;
    font-family: "Cinzel", "Times New Roman", serif;
    font-weight: 500;
    font-size: 21px;
    color: var(--plum);
    letter-spacing: 0.3px;
    white-space: nowrap;
  }

  .contact-list {
    position: absolute;
    left: 266px; top: 116px;
    list-style: none;
  }
  .contact-list li {
    display: flex;
    align-items: center;
    height: 16px;
    font-size: 11.5px;
    color: var(--ink);
    white-space: nowrap;
  }
  .contact-list svg { width: 10px; height: 10px; margin-right: 12px; fill: var(--plum); flex: none; }
  .domain { color: var(--plum); }

  .address-line {
    position: absolute;
    left: 16px; right: 14px; top: 260px;
    display: flex;
    align-items: center;
    gap: 8px;
    font-size: 11.5px;
    color: var(--ink);
    white-space: nowrap;
  }
  .address-line .rule { flex: 1; height: 1px; background: var(--accent); }
</style>
</head>
<body>
  <section class="card card--front" aria-label="Card front">
    <p class="firm-name">Law Office of<br>Denise R. Harlow</p>
  </section>

  <section class="card card--back" aria-label="Card back">
    <p class="firm-name">Law Office of<br>Denise R. Harlow</p>

    <h1 class="attorney-name">Denise R. Harlow</h1>

    <ul class="contact-list">
      <li>
        <svg viewBox="0 0 10 10" aria-hidden="true"><path d="M1 3.2C1 1.8 2.8 1 5 1s4 .8 4 2.2V4H7V3H3v1H1z"/><path d="M2 5.5 3.5 4h3L8 5.5V9H2z"/></svg>
        (855) 602-7318
      </li>
      <li>
        <svg viewBox="0 0 10 10" aria-hidden="true"><path d="M3 0h4a1 1 0 0 1 1 1v8a1 1 0 0 1-1 1H3a1 1 0 0 1-1-1V1a1 1 0 0 1 1-1zm0 1.5v6h4v-6zM5 8.2a.6.6 0 1 0 0 1.2.6.6 0 0 0 0-1.2z"/></svg>
        (917) 463-5071
      </li>
      <li>
        <svg viewBox="0 0 10 10" aria-hidden="true"><path d="M0 2h10v6H0zm1 .8V3l4 2.8L9 3v-.2z"/></svg>
        Denise@DeniseRHarlowLegal.test
      </li>
      <li>
        <svg viewBox="0 0 10 10" aria-hidden="true"><path d="M5 0a5 5 0 1 0 0 10A5 5 0 0 0 5 0zm-.5 1.1v1.7H3.1c.3-.9.8-1.5 1.4-1.7zm1 0c.6.2 1.1.8 1.4 1.7H5.5zM2.2 2.8H1.9a4 4 0 0 1 1.4-1.2c-.4.3-.8.8-1.1 1.2zM1 4.5h1.9v1H1zm2.8 0h.7v1h-.7zm1.7 0h.7v1h-.7zm1.6 0H9v1H7.1zM1.9 7.2h1.2c.3.8.8 1.4 1.4 1.7A4 4 0 0 1 1.9 7.2zm2.6 0v1.7c-.6-.2-1.1-.8-1.4-1.7zm1 0h1.4c-.3.9-.8 1.5-1.4 1.7z"/></svg>
        www.<span class="domain">DeniseRHarlowLegal</span>.test
      </li>
    </ul>

    <p class="address-line">
      <span class="rule"></span>
      528 E. 19th Street 7th Floor New York, NY 10583
      <span class="rule"></span>
    </p>
  </section>
</body>
</html>
```